Stories from Elm trifold brochure design

We are a start up company that will help seniors write their memoirs...beginning with a few ancestors and their heritage and continuing through their own history...how they would like to be remembered in the next generation. I envision a senior citizen at an older writing desk, writing her memoirs, with a book (maybe standing on top, leaning slightly) that has the words Stories from Elm.com on the back binding. OR maybe a senior couple walking into the sunset with the same book somewhere in the frame. Communicating the relevance of every life being significant to those that come after them...when a genealogy doesn't say enough about the details of one's life. Please note that I am open to the professionals own ideas...I am not locked into my concepts. I would like one or two phrases..."When A Genealogy Doesn't Say Enough" and/or "Every life legacy is a gift for the next generation to treasure" to be in the design.
A few documents are loaded that contain notes for our web designers. Maybe they will help you with our thoughts.

Reason: We have added some additional photos that might be useful.

Target Market(s)

Seniors and the baby boomer generation

Industry/Entity Type

Graphic Design

Requirements
Must have
• Stories from Elm
• Doris Whitcombe, M.A.
• 1-609-382-5171 (local)
• 1-866-4TALEKP (toll free)
• info@storiesfromelm.com
• storiesfromelm.com
Should not have
• Scripts that would be challenging for seniors to read.

```html
<!DOCTYPE html>
<html lang="en">
<head>
<meta charset="utf-8">
<title>Stories from Elm – Trifold Brochure</title>
<link rel="stylesheet" href="https://fonts.googleapis.com/css2?family=Cinzel:wght@400;500;600&family=Raleway:ital,wght@0,400;0,500;0,700;1,400&family=Open+Sans:wght@400;700&display=swap">
<style>
  :root{
    --stage:#43302a;
    --paper:#ffffff;
    --paper-shade:#f1f1f1;
    --ink:#2b2b2b;
    --ink-soft:#4a4a4a;
    --blue:#1f6fb6;
    --band-top:#31ade4;
    --band-bottom:#0d78bb;
    --gold:#c9a54a;
    --gold-light:#e6cf8a;
    --tick:#d23a2c;
    --fold:#cfcfcf;
  }
  *{box-sizing:border-box;margin:0;padding:0}
  html,body{width:1200px;height:935px;overflow:hidden}
  body{background:var(--stage);font-family:"Raleway",sans-serif;color:var(--ink);position:relative}
  .brochure{position:absolute;left:44px;top:38px;width:1112px;height:859px;display:flex;box-shadow:0 2px 10px rgba(0,0,0,.45)}
  .panel{position:relative;width:371px;height:100%;background:linear-gradient(180deg,var(--paper) 0%,var(--paper) 70%,var(--paper-shade) 100%);overflow:hidden}
  .panel + .panel{border-left:1px solid var(--fold)}
  .gold-rule{position:absolute;left:0;right:0;height:3px;background:linear-gradient(90deg,var(--gold),var(--gold-light),var(--gold))}
  .band{position:absolute;left:0;right:0;bottom:0;height:127px;background:linear-gradient(180deg,var(--band-top),var(--band-bottom));color:#fff;text-align:center}
  .photo{position:absolute;left:0;right:0}
  .logo-box{position:absolute;background:#fff;border:1px solid #d9d2c0;box-shadow:2px 3px 6px rgba(0,0,0,.25);display:flex;align-items:center;justify-content:center;text-align:center;font-family:"Raleway",sans-serif;font-weight:500;color:var(--gold)}
  .ico{width:12px;height:12px;vertical-align:-1px;margin-right:5px}

  /* left panel */
  .community-title{position:absolute;left:30px;top:27px;font-family:"Cinzel",serif;font-weight:500;font-size:22px;color:var(--blue);letter-spacing:.5px}
  .community-copy{position:absolute;left:29px;top:60px;width:320px;font-size:12.4px;line-height:15.4px;color:var(--ink-soft)}
  .intro-copy{position:absolute;left:29px;top:398px;width:320px;font-size:12.4px;line-height:15.4px;color:var(--ink-soft)}
  .group-list{position:absolute;left:33px;top:452px;list-style:none;font-size:12.4px;line-height:16.9px;color:var(--ink-soft)}
  .group-list li::before{content:"";display:inline-block;width:6px;height:6px;border-radius:50%;background:var(--gold);margin-right:8px;vertical-align:2px}
  .gift-copy{position:absolute;left:29px;top:565px;width:320px;font-size:12.4px;line-height:15.4px;color:var(--ink-soft)}
  .occasion-list{position:absolute;left:31px;top:619px;list-style:none;font-size:12.4px;line-height:16.9px;color:var(--ink-soft)}
  .occasion-list svg{width:11px;height:11px;margin-right:6px;vertical-align:-1px}
  .band-cta{padding-top:14px;font-size:18.5px;line-height:24px}
  .band-phone{margin-top:6px;font-family:"Open Sans",sans-serif;font-weight:700;font-size:20px;letter-spacing:.5px}
  .band-web{font-size:13px;margin-top:1px}

  /* middle panel */
  .vehicle-head{position:absolute;left:10px;right:10px;top:32px;text-align:center;font-family:"Cinzel",serif;font-weight:400;font-size:21.5px;line-height:28px;color:#1e1e1e;letter-spacing:.8px}
  .gift-card{position:absolute;left:33px;top:232px;width:302px;height:195px;background:linear-gradient(160deg,#fff,#ececec);box-shadow:1px 2px 5px rgba(0,0,0,.3)}
  .gift-card .bow-area{position:absolute;left:8px;top:0;width:120px;height:96px;background:linear-gradient(135deg,#e8cf86,#c49a3c 60%,#a8802e)}
  .gift-card h3{position:absolute;left:180px;top:16px;font-family:"Open Sans",sans-serif;font-weight:700;font-size:17px;line-height:23px;color:#222}
  .gift-fields{position:absolute;left:18px;top:98px;list-style:none;font-size:12.5px;line-height:24px;color:#333}
  .consult-cta{position:absolute;left:10px;right:10px;top:476px;text-align:center;font-family:"Open Sans",sans-serif;font-weight:700;font-size:18px;line-height:25.5px;color:var(--blue)}
  .finance-copy{position:absolute;left:10px;right:10px;top:576px;text-align:center;font-size:19px;line-height:25.5px;color:#222}
  .contact-grid{position:absolute;left:0;right:0;top:30px;font-size:12.2px;text-align:left}
  .contact-grid .addr{position:absolute;left:26px;top:30px;line-height:14px}
  .contact-grid .addr .ico{position:absolute;left:0;top:1px}
  .contact-grid .addr span{display:block;padding-left:15px}
  .contact-grid .lines{position:absolute;left:170px;top:6px;line-height:22px}

  /* right panel */
  .tagline{position:absolute;left:0;right:0;text-align:center;font-style:italic;font-size:20.5px;line-height:27px;color:#222}
  .question{padding-top:12px;font-family:"Cinzel",serif;font-size:19px;line-height:23.5px;letter-spacing:.6px}
</style>
</head>
<body>
<main class="brochure">

  <section class="panel panel-left">
    <h2 class="community-title">Community Sessions</h2>
    <p class="community-copy">We offer 12 weekly session packages for groups of<br>10 or more. If you and others in your retirement or<br>community group would like to begin your Memoirs<br>together, we can bring our expertise to you!</p>
    <div class="gold-rule" style="top:128px"></div>
    <div class="photo" style="top:133px;height:247px;background:linear-gradient(135deg,#e9e4da 0%,#c8b9a2 40%,#b18b6a 70%,#8e7a64 100%)" role="img" aria-label="Photo of a smiling group of seniors sharing a meal at a restaurant table"></div>
    <div class="gold-rule" style="top:380px"></div>
    <p class="intro-copy">We offer a free one hour introductory class to help<br>you understand the commitment involved and<br>how we can help.</p>
    <ul class="group-list">
      <li>Community Groups</li>
      <li>Church Groups</li>
      <li>Retirement Communities</li>
      <li>Veterans Posts</li>
      <li>Civic Club</li>
      <li>Hospice, etc..........</li>
    </ul>
    <div class="logo-box" style="left:215px;top:461px;width:120px;height:70px;font-size:12px">Stories from Elm</div>
    <p class="gift-copy">Don’t have time to be involved but have loved<br>ones you would like to immortalize? Stories from<br>Elm makes a great gift idea!</p>
    <ul class="occasion-list">
      <li><svg viewBox="0 0 12 12"><rect x=".5" y=".5" width="11" height="11" fill="#fff" stroke="#bbb"/><path d="M2.5 6.5l2.5 2.5 5-7" fill="none" stroke="var(--tick)" stroke-width="2"/></svg>Anniversary</li>
      <li><svg viewBox="0 0 12 12"><rect x=".5" y=".5" width="11" height="11" fill="#fff" stroke="#bbb"/><path d="M2.5 6.5l2.5 2.5 5-7" fill="none" stroke="var(--tick)" stroke-width="2"/></svg>Birthday</li>
      <li><svg viewBox="0 0 12 12"><rect x=".5" y=".5" width="11" height="11" fill="#fff" stroke="#bbb"/><path d="M2.5 6.5l2.5 2.5 5-7" fill="none" stroke="var(--tick)" stroke-width="2"/></svg>Christmas</li>
      <li><svg viewBox="0 0 12 12"><rect x=".5" y=".5" width="11" height="11" fill="#fff" stroke="#bbb"/><path d="M2.5 6.5l2.5 2.5 5-7" fill="none" stroke="var(--tick)" stroke-width="2"/></svg>Hanukah</li>
      <li><svg viewBox="0 0 12 12"><rect x=".5" y=".5" width="11" height="11" fill="#fff" stroke="#bbb"/><path d="M2.5 6.5l2.5 2.5 5-7" fill="none" stroke="var(--tick)" stroke-width="2"/></svg>Arrival of grandchildren/great grandchildren</li>
      <li><svg viewBox="0 0 12 12"><rect x=".5" y=".5" width="11" height="11" fill="#fff" stroke="#bbb"/><path d="M2.5 6.5l2.5 2.5 5-7" fill="none" stroke="var(--tick)" stroke-width="2"/></svg>Hospice</li>
    </ul>
    <div class="gold-rule" style="top:729px"></div>
    <footer class="band">
      <p class="band-cta">Call or email to schedule your<br>free introductory class today.</p>
      <p class="band-phone"><svg class="ico" style="width:16px;height:16px;vertical-align:-2px" viewBox="0 0 16 16"><path d="M4 1.5l2.5 3-1.5 2c.8 1.8 2.2 3.2 4 4l2-1.5 3 2.5-1.5 2.5C7.5 14 2 8.5 1.5 3z" fill="none" stroke="#fff" stroke-width="1.4"/></svg>1-609-382-5171</p>
      <p class="band-web"><svg class="ico" viewBox="0 0 12 12"><circle cx="6" cy="6" r="5" fill="none" stroke="#fff"/><path d="M1 6h10M6 1c-2.5 3-2.5 7 0 10M6 1c2.5 3 2.5 7 0 10" fill="none" stroke="#fff" stroke-width=".8"/></svg>www.storiesfromelm.com</p>
    </footer>
  </section>

  <section class="panel panel-middle">
    <h1 class="vehicle-head">Now you have a vehicle<br>to help you immortalize<br>your thoughts for the<br>future... specifically<br>for those who will<br>want to know!</h1>
    <div class="gift-card">
      <div class="bow-area" role="img" aria-label="Gold gift bow with ribbon across the card corner"></div>
      <h3>Gift Cards<br>Available</h3>
      <ul class="gift-fields">
        <li>Name:</li><li>Phone:</li><li>Email:</li><li>Best time to call:</li>
      </ul>
    </div>
    <p class="consult-cta">Call or email us to schedule a<br>free consultation individually<br>or as a group today.</p>
    <p class="finance-copy">Ask about available financing<br>if needed. We are committed<br>to your legacy!</p>
    <div class="gold-rule" style="top:729px"></div>
    <footer class="band">
      <div class="contact-grid">
        <p class="addr"><svg class="ico" viewBox="0 0 12 12"><path d="M6 11.5C3 8 2 6.5 2 4.5a4 4 0 018 0c0 2-1 3.5-4 7z" fill="#fff"/><circle cx="6" cy="4.5" r="1.5" fill="var(--band-bottom)"/></svg><span>Doris Whitcombe,</span><span>M.A.</span></p>
        <p class="lines">
          <span><svg class="ico" viewBox="0 0 12 12"><path d="M1 4c2-2 8-2 10 0l-1.5 1.5-1.5-1V3.5h-4v1l-1.5 1zM2.5 6h7l1 4.5h-9z" fill="#fff"/></svg>1-866-4TALEKP</span><br>
          <span><svg class="ico" viewBox="0 0 12 12"><rect x="1" y="2.5" width="10" height="7" fill="none" stroke="#fff"/><path d="M1 2.5l5 4 5-4" fill="none" stroke="#fff"/></svg>info@storiesfromelm.com</span><br>
          <span><svg class="ico" viewBox="0 0 12 12"><circle cx="6" cy="6" r="5" fill="none" stroke="#fff"/><path d="M1 6h10M6 1c-2.5 3-2.5 7 0 10M6 1c2.5 3 2.5 7 0 10" fill="none" stroke="#fff" stroke-width=".8"/></svg>www.storiesfromelm.com</span>
        </p>
      </div>
    </footer>
    <div class="logo-box" style="left:117px;top:679px;width:132px;height:78px;font-size:13px">Stories from Elm</div>
  </section>

  <section class="panel panel-right">
    <div class="logo-box" style="left:36px;top:40px;width:294px;height:172px;font-size:30px;border-color:var(--gold)">Stories from Elm</div>
    <p class="tagline" style="top:239px">Ordinary Lives............<br>Extraordinary Legacies</p>
    <div class="gold-rule" style="top:308px"></div>
    <div class="photo" style="top:314px;height:321px;background:linear-gradient(180deg,#e7d6c5 0%,#d9c6b2 35%,#b7b3ad 55%,#c4b6a6 80%,#d8c4ae 100%)" role="img" aria-label="Photo of a senior couple walking hand in hand barefoot along the beach at sunset"></div>
    <div class="gold-rule" style="top:638px"></div>
    <p class="tagline" style="top:657px">When a genealogy<br>doesn’t say enough!</p>
    <div class="gold-rule" style="top:729px"></div>
    <footer class="band">
      <p class="question">If you were alive in 100 years,<br>what would you share with<br>your descendants?</p>
      <p class="band-web" style="margin-top:6px"><svg class="ico" viewBox="0 0 12 12"><circle cx="6" cy="6" r="5" fill="none" stroke="#fff"/><path d="M1 6h10M6 1c-2.5 3-2.5 7 0 10M6 1c2.5 3 2.5 7 0 10" fill="none" stroke="#fff" stroke-width=".8"/></svg>www.storiesfromelm.com</p>
    </footer>
  </section>

</main>
</body>
</html>
```